KVL cards

Design business cards for renamed business. Korvane Lighting Limited is a leading contract designer of electronic lighting products sepcialising in LED lighting. Need a design that is simple but clear please. Cards for two persons requried.

Target Market(s)

Professional and technical

Industry/Entity Type

Business

Font styles to use
Sans Serif
Other font styles liked:
• tahoma

Colors
ffcf3e

```html
<!DOCTYPE html>
<html lang="en">
<head>
<meta charset="utf-8">
<title>Korvane Lighting Limited – Business Card</title>
<link rel="stylesheet" href="https://fonts.googleapis.com/css2?family=Michroma&display=swap">
<style>
  :root {
    --page-bg: #e4e4e2;
    --card-dark: #1f1f20;
    --card-mid: #3a3a3b;
    --accent-blue: #35a9e0;
    --text-white: #f4f4f4;
    --text-soft: #d6d6d6;
  }
  * { margin: 0; padding: 0; box-sizing: border-box; }
  html, body {
    width: 1200px;
    height: 1024px;
    overflow: hidden;
    background: var(--page-bg);
    font-family: "Michroma", "Tahoma", sans-serif;
  }
  .canvas {
    width: 1200px;
    height: 1024px;
    display: flex;
    align-items: center;
    justify-content: center;
  }
  .business-card {
    position: relative;
    width: 500px;
    height: 860px;
    border-radius: 6px;
    background:
      radial-gradient(ellipse at 30% 35%, var(--card-mid) 0%, rgba(58,58,59,0) 60%),
      linear-gradient(160deg, #2c2c2d 0%, var(--card-dark) 100%);
    box-shadow: 0 18px 40px rgba(0,0,0,0.28);
    color: var(--text-white);
  }
  .brand-block {
    position: absolute;
    top: 90px;
    left: 56px;
    right: 48px;
    display: flex;
    align-items: center;
    gap: 16px;
  }
  .brand-dot {
    flex: 0 0 auto;
    width: 22px;
    height: 22px;
    border-radius: 50%;
    background: var(--accent-blue);
  }
  .brand-name {
    font-size: 27px;
    line-height: 1.3;
    color: var(--accent-blue);
    text-transform: uppercase;
    letter-spacing: 1px;
  }
  .person {
    position: absolute;
    top: 400px;
    left: 56px;
  }
  .person-role {
    font-size: 17px;
    color: var(--text-soft);
    letter-spacing: 1px;
    margin-bottom: 8px;
  }
  .person-name {
    font-size: 32px;
    color: var(--text-white);
    letter-spacing: 2px;
  }
  .contact-list {
    position: absolute;
    top: 530px;
    left: 56px;
    list-style: none;
  }
  .contact-item {
    display: flex;
    align-items: center;
    gap: 22px;
    height: 62px;
    font-size: 22px;
    letter-spacing: 1px;
    text-transform: uppercase;
  }
  .contact-icon {
    width: 30px;
    height: 30px;
    flex: 0 0 auto;
  }
</style>
</head>
<body>
<main class="canvas">
  <article class="business-card" aria-label="Korvane Lighting Limited business card">
    <header class="brand-block">
      <span class="brand-dot" aria-hidden="true"></span>
      <h1 class="brand-name">Korvane Lighting Limited</h1>
    </header>

    <section class="person">
      <p class="person-role">CEO</p>
      <h2 class="person-name">YOUR NAME</h2>
    </section>

    <ul class="contact-list">
      <li class="contact-item">
        <svg class="contact-icon" viewBox="0 0 30 30" aria-hidden="true">
          <circle cx="15" cy="15" r="13" fill="none" stroke="var(--accent-blue)" stroke-width="2.5"/>
          <path d="M11 9 q-3 6 2 11 q4 3 6 1 l-2 -3 l-2 1 q-3 -2 -3 -5 l2 -1 z" fill="var(--accent-blue)"/>
        </svg>
        <span>0777 777 777</span>
      </li>
      <li class="contact-item">
        <svg class="contact-icon" viewBox="0 0 30 30" aria-hidden="true">
          <circle cx="15" cy="15" r="13" fill="none" stroke="var(--accent-blue)" stroke-width="2.5"/>
          <path d="M6 15 l3 -3 l3 6 l3 -6 l3 6 l3 -6 l3 3" fill="none" stroke="var(--accent-blue)" stroke-width="2"/>
        </svg>
        <span>website.com</span>
      </li>
      <li class="contact-item">
        <svg class="contact-icon" viewBox="0 0 30 30" aria-hidden="true">
          <circle cx="15" cy="15" r="13" fill="var(--accent-blue)"/>
          <text x="15" y="20" text-anchor="middle" font-size="14" font-family="Tahoma, sans-serif" fill="var(--card-dark)">@</text>
        </svg>
        <span>your@email.com</span>
      </li>
    </ul>
  </article>
</main>
</body>
</html>
```